Video production company website

VistaKeel Productions is a video and photography production company serving many Fortune 500 clients traveling to Hawaii and International Destinations. Our primary focus is the Corporate and Incentive group market, and offer both photography and video services. In addition, we also create custom marketing, sales, art, and real estate productions.

Target Market(s)

Corporate Incentive Travel Groups

Industry/Entity Type

Videography

Number of Pages Required

4 page

Requirements
Must have
• see doc with content. This will ultimately be needed to be a wordpress design so we can update ourselves.
Nice to have
• sleek design, professional, cutting edge, modern
Should not have
• too much Hawaii Feel, some ok but we do travel international

```html
<!DOCTYPE html>
<html lang="en">
<head>
<meta charset="utf-8">
<title>VistaKeel Productions</title>
<link href="https://fonts.googleapis.com/css2?family=Arvo:wght@400;700&family=Merriweather:wght@300;400&display=swap" rel="stylesheet">
<style>
:root{
  --purple:#6b2381;
  --purple-band:#7b2d91;
  --purple-btn:#6e2585;
  --ink:#222;
  --grey:#555;
  --white:#fff;
  --navy:#101a57;
  --black:#000;
}
*{margin:0;padding:0;box-sizing:border-box}
html,body{width:1200px;height:3352px;overflow:hidden}
body{position:relative;background:var(--white);font-family:'Merriweather',Georgia,serif;color:var(--ink)}
section,header,footer{position:absolute;left:0;width:1200px}
.abs{position:absolute}
.slab{font-family:'Arvo',Georgia,serif}
.btn{position:absolute;display:flex;align-items:center;justify-content:center;background:var(--purple-btn);color:var(--white);font-family:'Arvo',Georgia,serif;font-size:15px;text-transform:uppercase;border:1px solid rgba(255,255,255,.5)}

/* header / hero */
.hero{top:0;height:619px}
.hero-photo{position:absolute;inset:0;background:linear-gradient(180deg,#8fb0c4 0%,#b9c7b6 18%,#6f7f6e 30%,#4a4c55 55%,#8a6f57 80%,#a47d5b 100%)}
.site-bar{position:absolute;top:0;left:0;width:1200px;height:107px;background:rgba(255,255,255,.55)}
.brand{position:absolute;left:183px;top:16px;width:250px;text-align:center}
.brand-name{font-family:'Arvo',Georgia,serif;font-size:26px;color:#333}
.brand-tag{font-family:'Arvo',Georgia,serif;font-size:14px;color:#222;margin-top:12px}
.nav{position:absolute;left:530px;top:40px;display:flex;gap:30px;align-items:center;font-family:'Arvo',Georgia,serif;font-weight:700;font-size:15px;color:#111}
.nav .active{color:var(--purple)}
.hero-caption{position:absolute;top:432px;width:1200px;text-align:center;font-family:'Arvo',Georgia,serif;font-weight:700;font-size:38px;color:var(--white);text-shadow:0 2px 6px rgba(0,0,0,.6)}

/* welcome */
.welcome{top:619px;height:492px}
.welcome-title{position:absolute;left:172px;top:62px;font-family:'Arvo',Georgia,serif;color:#444;font-size:33px;line-height:40px}
.welcome-title strong{display:block;color:var(--purple);font-weight:700}
.welcome-text{position:absolute;left:172px;top:180px;width:345px;font-size:11.5px;line-height:21px;color:var(--grey);font-weight:300}
.shot{position:absolute;box-shadow:0 4px 14px rgba(0,0,0,.25)}
.shot-swim{left:599px;top:-56px;width:429px;height:311px;background:linear-gradient(180deg,#4b8fd6 0%,#9cc6ea 40%,#2d76b8 70%,#1e5f9e 100%)}
.shot-couple{left:545px;top:201px;width:302px;height:219px;background:linear-gradient(180deg,#e9a040 0%,#c87a2a 40%,#3d4a2c 75%,#2c3520 100%)}

/* videos */
.videos{top:1111px;height:565px;background:linear-gradient(180deg,#c9b79a 0%,#a88f6e 25%,#5e4c38 55%,#3b3125 80%,#6a5a48 100%)}
.section-title{position:absolute;width:1200px;text-align:center;font-family:'Arvo',Georgia,serif;font-weight:700;font-size:33px;color:var(--purple)}
.player{position:absolute;left:360px;top:109px;width:480px;height:320px;border:3px solid #eee;background:linear-gradient(180deg,#6fa2d2 0%,#9cc4d8 35%,#5b8a3a 60%,#6fa046 100%)}
.player-bar{position:absolute;left:0;bottom:0;width:100%;height:28px;background:linear-gradient(#eee,#c9c9c9)}
.play-note{position:absolute;top:480px;width:1200px;display:flex;justify-content:center;align-items:center;gap:12px;font-size:14px;color:var(--white)}
.play-note .btn,.gallery-note .btn{position:static;height:46px;padding:0 18px}

/* photography */
.photography{top:1676px;height:526px}
.strip{position:absolute;top:148px;left:0;display:flex;width:1200px;height:199px}
.strip div{flex:1}
.gallery-note{position:absolute;top:397px;width:1200px;display:flex;justify-content:center;align-items:center;gap:14px;font-size:14px;color:var(--grey)}

/* newsletter */
.newsletter{top:2202px;height:183px;background:var(--purple-band);color:var(--white)}
.nl-title{position:absolute;left:172px;top:58px;font-family:'Arvo',Georgia,serif;font-size:26px;letter-spacing:1px}
.nl-sub{position:absolute;left:172px;top:98px;font-size:13px}
.nl-input{position:absolute;left:548px;top:62px;width:353px;height:51px;border:1px solid rgba(255,255,255,.7);padding:0 16px;display:flex;align-items:center;font-size:12px;color:rgba(255,255,255,.85)}
.nl-btn{position:absolute;left:910px;top:62px;width:118px;height:51px;background:var(--black);color:var(--white);font-family:'Arvo',Georgia,serif;font-weight:700;font-size:17px;display:flex;align-items:center;justify-content:center;letter-spacing:1px;border:1px solid rgba(255,255,255,.7)}

/* contact */
.contact{top:2385px;height:967px;background:linear-gradient(180deg,#9aa7e3 0%,#b7a9d8 18%,#d9a7b2 32%,#6b5d9e 45%,#2a2f7c 60%,var(--navy) 75%,var(--navy) 100%)}
.contact-title{position:absolute;top:66px;width:1200px;text-align:center;font-family:'Arvo',Georgia,serif;font-weight:700;font-size:33px;color:#111}
.contact-sub{position:absolute;top:106px;width:1200px;text-align:center;font-family:'Arvo',Georgia,serif;font-weight:700;font-size:26px;color:var(--purple)}
.field{position:absolute;left:389px;width:422px;height:42px;background:rgba(255,255,255,.3);border:1px solid rgba(255,255,255,.5);padding:10px 16px;font-size:13px;color:rgba(255,255,255,.85)}
.send{position:absolute;left:389px;top:516px;width:422px;height:54px;background:var(--purple-btn);border:1px solid rgba(255,255,255,.6);color:var(--white);font-family:'Arvo',Georgia,serif;font-weight:700;font-size:22px;display:flex;align-items:center;justify-content:center;letter-spacing:1px}
.foot-title{position:absolute;top:636px;width:1200px;text-align:center;font-family:'Arvo',Georgia,serif;font-weight:700;font-size:32px;color:var(--white)}
.foot-addr{position:absolute;top:703px;width:1200px;text-align:center;font-size:14px;color:var(--white)}
.foot-phones{position:absolute;top:740px;width:1200px;display:flex;justify-content:center;gap:30px;font-family:'Arvo',Georgia,serif;font-weight:700;font-size:22px;color:var(--white)}
.foot-phones span{display:flex;align-items:center;gap:8px}
.follow{position:absolute;top:805px;width:1200px;text-align:center;font-size:13px;color:var(--white)}
.socials{position:absolute;top:835px;width:1200px;display:flex;justify-content:center;gap:8px}
.socials span{width:40px;height:40px;border:2px solid var(--white);border-radius:50%}
.copyright{position:absolute;top:912px;width:1200px;text-align:center;font-size:10px;color:rgba(255,255,255,.8)}
</style>
</head>
<body>

<header class="hero">
  <div class="hero-photo" role="img" aria-label="Large travel group posing together on the sun deck of a river cruise ship with two branded umbrellas"></div>
  <div class="site-bar"></div>
  <div class="brand">
    <div class="brand-name">VistaKeel Productions</div>
    <div class="brand-tag">The Best of the Best</div>
  </div>
  <nav class="nav">
    <span class="active">Home</span><span>About Us</span><span>Photography</span><span>Video</span><span>Contact Us</span>
    <svg width="16" height="16" viewBox="0 0 16 16"><circle cx="6.5" cy="6.5" r="4.5" fill="none" stroke="#111" stroke-width="2"/><line x1="10" y1="10" x2="14" y2="14" stroke="#111" stroke-width="2.4"/></svg>
  </nav>
  <h1 class="hero-caption">Enjoy the unforgettable tour to Hawaii !</h1>
</header>

<section class="welcome">
  <h2 class="welcome-title">Welcome to<strong>VistaKeel Productions</strong></h2>
  <p class="welcome-text">VistaKeel Productions is a video and photography production company serving many Fortune 500 clients in Hawaii and Internationally. Our primary focus is the Corporate and Incentive group market, and offer both photography and video services. In addition, we also create custom marketing, sales, art, and real estate productions.</p>
  <div class="btn" style="left:172px;top:373px;width:188px;height:47px;text-transform:none;font-size:15px">Contact Us Today</div>
  <div class="shot shot-swim" role="img" aria-label="Guests snorkelling and paddling on boards in clear blue ocean water"></div>
  <div class="shot shot-couple" role="img" aria-label="Couple wearing leis posing at sunset by the ocean"></div>
</section>

<section class="videos" role="img" aria-label="Blurred sunset over a beach" style="">
  <h2 class="section-title" style="top:44px">Watch Our Sample Videos.</h2>
  <div class="player">
    <div class="abs" style="inset:0 0 28px 0" role="img" aria-label="Video still of a group jumping joyfully on a golf course"></div>
    <div class="player-bar">
      <svg width="474" height="28" viewBox="0 0 474 28">
        <polygon points="12,9 12,19 20,14" fill="#333"/>
        <rect x="34" y="12" width="230" height="4" fill="#999"/>
        <rect x="34" y="12" width="110" height="4" fill="#c0282d"/>
        <circle cx="144" cy="14" r="5" fill="#ddd" stroke="#777"/>
        <text x="290" y="18" font-size="9" fill="#333" font-family="Arial, sans-serif">0:47 / 3:29</text>
        <path d="M360 11h4l5-4v14l-5-4h-4z" fill="#333"/>
        <rect x="378" y="12" width="60" height="4" fill="#c0282d"/>
        <rect x="450" y="8" width="12" height="12" fill="none" stroke="#333" stroke-width="1.6"/>
      </svg>
    </div>
  </div>
  <p class="play-note">Please <span class="btn">Contact Us</span> for you next project and for a password to watch our sample videos.</p>
</section>

<section class="photography">
  <h2 class="section-title" style="top:70px">Watch Our Photography</h2>
  <div class="strip">
    <div role="img" aria-label="Videographer filming a group on a lawn" style="background:linear-gradient(180deg,#7ab2e0,#6a8a4c)"></div>
    <div role="img" aria-label="Island dancers performing at night" style="background:linear-gradient(180deg,#2a1a12,#8a3a22)"></div>
    <div role="img" aria-label="Guests kayaking on blue water" style="background:linear-gradient(180deg,#6fb0e4,#1c64b0)"></div>
    <div role="img" aria-label="Costumed performer at an illuminated night event" style="background:linear-gradient(180deg,#0e0e1e,#6a3ea0)"></div>
    <div role="img" aria-label="Golfer swinging on a coastal course" style="background:linear-gradient(180deg,#c8d4dc,#6c7a6a)"></div>
    <div role="img" aria-label="Couple posing in a tropical garden at a resort" style="background:linear-gradient(180deg,#5e6f3a,#a87a4c)"></div>
  </div>
  <p class="gallery-note">Please <span class="btn">Contact Us</span> for a custom quote. Please <span class="btn">Click Here</span> for our gallery.</p>
</section>

<section class="newsletter">
  <h2 class="nl-title">NEWSLETTER SIGN-UP</h2>
  <p class="nl-sub">We make sure you do not miss any news</p>
  <div class="nl-input">Enter you e-mail...</div>
  <div class="nl-btn">SIGNUP</div>
</section>

<footer class="contact">
  <div class="abs" style="left:0;top:0;width:1200px;height:620px" role="img" aria-label="Palm tree silhouettes reflected in still water at twilight"></div>
  <h2 class="contact-title">We look forward to hearing from you.</h2>
  <p class="contact-sub">Aloha, Daniel Ashby-President</p>
  <div class="field" style="top:170px">Name</div>
  <div class="field" style="top:223px">Company Info</div>
  <div class="field" style="top:275px">Phone</div>
  <div class="field" style="top:326px">Email</div>
  <div class="field" style="top:378px;height:105px">Message</div>
  <div class="send">SEND</div>

  <h2 class="foot-title">Contact us</h2>
  <p class="foot-addr">VistaKeel Productions, LLC,&nbsp; P.O. Box 412-118,&nbsp; Makena HI 96790</p>
  <div class="foot-phones">
    <span><svg width="26" height="26" viewBox="0 0 26 26"><circle cx="13" cy="13" r="11.5" fill="none" stroke="#fff" stroke-width="2"/><path d="M9 7c1 0 2 2 2 3s-1 1-1 2 2 4 4 4 1-1 2-1 3 1 3 2-1 2-3 2c-4 0-9-5-9-9 0-2 1-3 2-3z" fill="#fff"/></svg>(808) 555.0142</span>
    <span><svg width="26" height="26" viewBox="0 0 26 26"><circle cx="13" cy="13" r="11.5" fill="none" stroke="#fff" stroke-width="2"/><rect x="7" y="10" width="12" height="8" rx="1" fill="#fff"/><rect x="9" y="7" width="8" height="4" fill="none" stroke="#fff" stroke-width="1.5"/></svg>(808) 555.0187</span>
  </div>
  <p class="follow">Follow Us On:</p>
  <div class="socials"><span></span><span></span><span></span><span></span></div>
  <p class="copyright">© 2016 VistaKeel Productions, LLC. All rights reserved.</p>
</footer>

</body>
</html>
```